依頼概要
■依頼目的/概要
電子書籍を出版いたしますので、表紙デザインをお願いいたします。

-------------
■本のタイトル
灯火(ともしび)

【サブタイトル】
~静かな朝を迎える言葉の書~
※あとから修正依頼あり

<著者>
柏木遥斗

<おまけ特典>
シベリア晴郎vs櫻庭露樹 秘密の対談動画

---------------------------
納品は、
2,560×1,600ピクセルのJPEGと元データをお願い致したく。

----著者プロフィール ご参考まで---------
《柏木遥斗》
青森県三沢市生まれ
幼少期の極貧生活と虐待により、小学三年生9歳から朝刊夕刊の新聞配達や集金をこなしながら、2つの不労所得を得るビジネスプランを完成させる。小学生時代に稼いだ金額は一千万円。24歳で起業後、フランチャイズの店舗経営を始め10店舗まで右肩上がりで経営を成功させたのち売却。追って、自由が丘と溝の口に、水晶天然石の店舗KOVUSをオープン。

現在は複数の会社で事業展開の他、各所の著名大企業からヘッドハンティングされ社外取締役などを務めながら、世界中の富豪層からも愛され何かと声をかけられる摩訶不思議な強運の持ち主、人呼んで開運マスター。

「アホと素直と行動力、プラス笑顔」を提唱し、トイレ掃除や全捨離の実践者でもある。
売れっ子芸人並みの秀逸なギャグセンスに、少年のような真っ直ぐでピュアな心と、ゴロスケのような豪快さを併せ持つ人柄に惹きつけられるファンも多く、当たり過ぎる超適当なタロット占い、恋愛や仕事、人間関係などに悩む方の人生相談会なども好評を得ている。
いまや、全国各地のみならず世界各所から、心のあり方や開運に特化した講演を依頼される超人気講師。

オンラインサロンを開設しコミュニティは大盛況で運営中。柏木の生き様や実践法、表に出せない極秘情報はもちろん、登場する超個性的な師匠や偉人たちに魅了され、世界中から人気を集めている。
2019年夏に開設したYoutubeチャンネルもすでに16万人の登録者を超えるなど大ブレイク中。

著書に、自らが支援している子供たちを描いた『僕らは丘の上でいつも笑っている仲間たち。草原の学び舎「草原の仲間たち」の物語』、トイレ掃除と開運についての名書『台所の精霊が教えた内緒の招福術 福鍋の定理』、電子書籍『福鍋のこころえ』、『7つを減らせば毎日かるくなる!総片付』、リバーサイド出版社『暮らしの巡りが整うコツを集めてみた』、『財布が喜ぶありとあらゆる習慣を調べてみた』など多数。
--------------------------
■デザイン要望

シンプル イズ ベスト。白バックに黒字の明朝体。
上品で視認性の高いもの、しかし機能的になりすぎず余白美を醸しているもの。

イメージ画像①、②の丸枠に、著者画像を組み込んでいただきたいです。
(※下記、添付ファイルをご参照くださいませ)

ーーーーご参考までーー----------------
■デザインイメージのヒントとなる『あとがき』の抜粋の一部を、下記に掲載します。

(あとがき より)
本書を通じて、宇宙法則、風水、タイムマネジメントといった多岐にわたる分野の智慧と、様々な体験と深い教養に基づいた森羅万象に精通するモルダ冬彦先生の貴重なお話の数々が散りばめられています。先生が立命するきっかけとなった出逢いや回想録にも触れ、運とは何か、ということや、運を強くする方法について語っていただきました。

歴史を振り返ってみた時に、かつての我が国、幕末の日本にも、今現在の僕たちが体験しているような混沌の時代がありました。青天の霹靂のような出来事が多発し、情報が錯綜する中で、これまでの常識や価値観は見事に崩れ落ちています。パラダイムシフトになぞらえられる、令和の今のこの世にご縁があって集まった僕たちには、時代を超え、何か大切な命題を叩きつけられているように思います。

あえてこの時代に生まれた私たちの魂の欲するところは何なのか。人生の使命とは?

冬彦先生は、そんな問いに挑戦し、各々の人生に挑戦する僕たち現代人に、いつもたくさんのヒントを提示してくださいます。今回は幕末に生きたスピリチュアル的思想の先駆者、杉村東巌先生の教えを引用し、魂の成長錬磨のよりシンプルかつ具体的な方法をもご指南いただけました。(以上 一部抜粋)

※その他イラストや写真等素材を使用される場合には、商用利用可の素材をお願いします。

■その他、デザインを考えるのに必要な情報などありましたら、
お答えしますので、遠慮なくお尋ねくださいませ。

よろしくお願い申し上げます。
たくさんのご応募誠にありがとうございました。
皆様の作品を大切に拝見し、ご尽力に感謝の気持ちでいっぱいでございます。

著者のもと鋭意選定をすすめておりますので、今しばらくお待ちいただけますと幸いに存じます。

ご高配のほどよろしくお願い申し上げます。

デザイン要望にもとづき、参考文より汲み取って頂いた
世界観が表現されていて、とても素晴らしい作品です。

著者が一番気に入ったそうなので
こちらを選定させていただきました。

この度は貴重なお時間と労力をお掛けくださり
素晴らしい作品をご応募いただきまして
本当にどうもありがとうございました。

どれも逸品で大変迷いましたが
今回はこちらに決めさせていただきました。

せっかくご応募いただきましたのに
選定できない方々、
誠に申し訳ございません。

今後ともご縁がございましたら
次回もどうぞよろしくお願い致します!

皆様のますますのご活躍を心より祈念致しております。

本当にどうもありがとうございました。

```html
<!DOCTYPE html>
<html lang="ja">
<head>
<meta charset="utf-8">
<title>灯火 ― 静かな朝を迎える言葉の書</title>
<link rel="stylesheet" href="https://fonts.googleapis.com/css2?family=Shippori+Mincho+B1:wght@500;700;800&family=Noto+Serif+JP:wght@400;600;700;900&display=swap">
<style>
  :root {
    --paper: #ffffff;
    --ink: #141414;
    --accent: #c8102e;
    --rule: #3a3a3a;
  }
  * { margin: 0; padding: 0; box-sizing: border-box; }
  html, body { width: 750px; height: 1200px; overflow: hidden; background: var(--paper); }
  .cover {
    position: relative;
    width: 750px; height: 1200px;
    background: var(--paper);
    color: var(--ink);
    font-family: "Shippori Mincho B1", "Noto Serif JP", serif;
    text-align: center;
  }
  .author {
    position: absolute; top: 14px; left: 0; right: 0;
    font-size: 46px; font-weight: 700; letter-spacing: 2px;
  }
  .author-rule {
    position: absolute; top: 92px; left: 75px; width: 600px; height: 2px;
    background: var(--rule);
  }
  .title {
    position: absolute; top: 178px; left: 0; right: 0;
    font-family: "Noto Serif JP", serif;
    font-size: 272px; font-weight: 900; line-height: 1;
    letter-spacing: 4px;
  }
  .title-roman {
    position: absolute; top: 434px; left: 0; right: 0;
    font-family: "Noto Serif JP", serif;
    font-size: 36px; font-weight: 400; letter-spacing: 3px;
  }
  .subtitle {
    position: absolute; top: 492px; left: 0; right: 0;
    font-size: 38px; font-weight: 700; color: var(--accent);
    letter-spacing: 1px;
  }
  .bonus-label {
    position: absolute; top: 786px; left: 237px; width: 276px; height: 76px;
    border: 3px solid var(--ink); border-radius: 10px;
    font-size: 38px; font-weight: 700; line-height: 70px;
    letter-spacing: 2px;
  }
  .bonus-video {
    position: absolute; top: 900px; left: 195px; width: 360px; height: 212px;
    border: 7px solid var(--ink); border-radius: 6px;
    background: var(--paper); overflow: hidden;
  }
  .bonus-video .guests {
    margin-top: 22px;
    font-size: 29px; font-weight: 700; letter-spacing: -0.5px;
  }
  .bonus-video .topic {
    margin-top: 4px;
    font-size: 36px; font-weight: 800; color: var(--accent);
  }
  .player-bar {
    position: absolute; left: 0; right: 0; bottom: 0; height: 44px;
    background: var(--ink);
  }
  .player-bar svg { display: block; }
</style>
</head>
<body>
  <main class="cover">
    <p class="author">柏木遥斗</p>
    <div class="author-rule"></div>

    <h1 class="title">灯火</h1>
    <p class="title-roman">- Tomoshibi -</p>
    <p class="subtitle">静かな朝を迎える言葉の書</p>

    <div class="bonus-label">おまけ特典</div>

    <section class="bonus-video">
      <p class="guests">モルダ冬彦vs柏木遥斗</p>
      <p class="topic">秘密の対談動画</p>
      <div class="player-bar">
        <svg width="346" height="44" viewBox="0 0 346 44" aria-hidden="true">
          <rect x="0" y="0" width="346" height="4" fill="#555"/>
          <rect x="0" y="0" width="120" height="4" fill="var(--accent)"/>
          <circle cx="120" cy="2" r="5" fill="var(--accent)"/>
          <polygon points="14,14 14,32 28,23" fill="#fff"/>
          <polygon points="38,14 38,32 50,23" fill="#fff"/>
          <rect x="51" y="14" width="3" height="18" fill="#fff"/>
          <polygon points="66,19 72,19 79,13 79,33 72,27 66,27" fill="#fff"/>
          <path d="M84 17 Q89 23 84 29" stroke="#fff" stroke-width="2" fill="none"/>
          <rect x="296" y="16" width="16" height="14" fill="none" stroke="#fff" stroke-width="2"/>
          <rect x="322" y="15" width="14" height="16" fill="none" stroke="#fff" stroke-width="2"/>
        </svg>
      </div>
    </section>
  </main>
</body>
</html>
```